Medical Clinic Group Looking for Website Design

We own and operate medical clinics and are looking looking to revamp our website. Our current website is www.marlowcarepartners.ca We need our website to be more functional, user friendly, and easier to maintain.

```html
<!DOCTYPE html>
<html lang="en">
<head>
<meta charset="utf-8">
<title>Marlow Care Partners</title>
<link href="https://fonts.googleapis.com/css2?family=Lato:wght@400;700&family=Montserrat:wght@400;500;600&family=Catamaran:wght@600;700&family=Arimo:wght@400&display=swap" rel="stylesheet">
<style>
:root{
  --teal:#35d3dc;
  --teal-dark:#1fb9c3;
  --teal-pale:#e9fbfd;
  --ink:#2f2f2f;
  --muted:#555;
  --band:#efefef;
  --white:#fff;
  --bar:#3b3b3b;
}
*{box-sizing:border-box;margin:0;padding:0}
html,body{width:1200px;height:3819px;overflow:hidden}
body{position:relative;background:var(--white);font-family:'Lato',sans-serif;color:var(--ink)}
.abs{position:absolute}
.btn{position:absolute;display:flex;align-items:center;justify-content:center;background:var(--teal);color:var(--white);border-radius:27px;font:600 15px 'Montserrat',sans-serif;text-decoration:none}

/* header */
.brand{left:66px;top:40px;display:flex;align-items:center;gap:14px;font:400 34px 'Lato',sans-serif;color:var(--teal)}
.brand-dot{width:40px;height:40px;border-radius:50%;background:var(--teal)}
.nav{left:488px;top:50px;display:flex;gap:36px;font:500 15px 'Montserrat',sans-serif;color:var(--ink)}
.nav-book{left:948px;top:33px;width:151px;height:53px}

/* hero */
.hero{left:0;top:0;width:1200px;height:825px;background:linear-gradient(90deg,#f6f6f6 0%,#eef1f2 40%,#d9eef2 70%,#cfe6ec 100%)}
.hero-photo{left:520px;top:90px;width:680px;height:735px;background:radial-gradient(ellipse at 55% 45%,#6fc4d2 0%,#a9d9e2 45%,rgba(220,238,242,0) 75%)}
.hero-title{left:128px;top:326px;font:700 50px 'Catamaran',sans-serif;color:var(--ink)}
.hero-title span{color:var(--teal)}
.hero-sub{left:128px;top:396px;font:400 25px/39px 'Catamaran',sans-serif;color:var(--ink)}
.hero-book{left:119px;top:495px;width:151px;height:52px}
.tile{position:absolute;top:752px;width:299px;height:129px;background:linear-gradient(135deg,#3cd0d9,#2cc3cd);display:flex;align-items:center;justify-content:center;gap:22px;font:700 32px 'Catamaran',sans-serif;color:var(--white)}
.tile-arrow{width:56px;height:56px;border-radius:50%;background:var(--white);display:flex;align-items:center;justify-content:center}

/* about */
.about-frame-top{left:82px;top:979px;width:550px;height:16px;background:var(--teal);clip-path:polygon(0 0,100% 0,97% 100%,0 100%)}
.about-frame-left{left:82px;top:979px;width:14px;height:532px;background:var(--teal);clip-path:polygon(0 0,100% 0,100% 100%,0 98%)}
.about-photo{left:95px;top:995px;width:550px;height:532px;background:linear-gradient(160deg,#e8eef0 0%,#dfe7ea 50%,#c8d6da 100%)}
.about-card{left:562px;top:1040px;width:592px;height:437px;background:var(--teal-pale);border-radius:32px;padding:34px 38px}
.about-card h2{font:700 31px 'Lato',sans-serif;margin-bottom:22px}
.about-card h3{font:400 20px/30px 'Lato',sans-serif;margin-bottom:18px;padding-left:2px}
.about-card p{font:400 15px/30px 'Lato',sans-serif;color:var(--ink)}
.about-more{left:593px;top:1385px;width:151px;height:52px}

/* services */
.band{left:0;width:1200px;background:var(--band)}
.section-title{position:absolute;left:0;width:1200px;text-align:center;font:700 32px 'Lato',sans-serif;color:var(--ink)}
.svc{position:absolute;top:1740px;width:298px;background:var(--white);border-radius:6px;box-shadow:0 2px 10px rgba(0,0,0,.06);padding:32px 0 0}
.svc.active{background:var(--teal);color:var(--white)}
.svc-icon{width:112px;height:112px;margin:0 auto;border-radius:50%;background:var(--teal);border:8px solid #c9f3f6;display:flex;align-items:center;justify-content:center}
.svc.active .svc-icon{background:var(--white);border-color:#8fe6eb}
.svc h4{text-align:center;font:600 23px 'Montserrat',sans-serif;color:var(--teal);margin:32px 0 22px}
.svc.active h4{color:var(--white)}
.svc ul{list-style:none;padding:0 12px 0 18px}
.svc li{display:flex;gap:10px;font:500 17px/20px 'Montserrat',sans-serif;margin-bottom:19.5px}
.svc li svg{flex:0 0 16px;margin-top:2px}
.carousel-arrow{position:absolute}

/* access */
.access-copy{left:205px;top:2432px;width:790px;text-align:center;font:400 14.5px/30px 'Lato',sans-serif;color:var(--ink)}
.access-card{position:absolute;top:2564px;width:261px;height:285px;background:#fafafa;border-radius:10px;box-shadow:0 2px 12px rgba(0,0,0,.06);text-align:center}
.access-art{width:110px;height:100px;margin:28px auto 0;border-radius:50%;background:radial-gradient(circle at 60% 40%,#d7f6f8 0%,#bdeef2 60%,#e7fafb 100%)}
.access-card h4{font:700 21px 'Lato',sans-serif;margin-top:22px}
.access-card .btn{left:59px;top:197px;width:151px;height:52px}

/* testimonials */
.quote{position:absolute;top:3067px;width:470px;height:258px;background:var(--white);border-radius:18px;box-shadow:0 2px 10px rgba(0,0,0,.06)}
.quote-photo{position:absolute;left:25px;top:30px;width:103px;height:102px;background:linear-gradient(180deg,#f2f2f2,#cfd6d8);border-right:2px solid var(--teal);border-bottom:2px solid var(--teal)}
.quote-name{position:absolute;left:25px;top:144px;font:500 17px 'Montserrat',sans-serif}
.quote-role{position:absolute;left:25px;top:173px;font:400 15px 'Montserrat',sans-serif;color:var(--ink)}
.quote-rule{position:absolute;left:160px;top:25px;width:1px;height:208px;background:#ddd}
.quote-text{position:absolute;left:177px;top:27px;width:266px;font:400 15.5px/25.7px 'Montserrat',sans-serif;text-align:justify;color:var(--ink)}

/* footer */
.footer{left:0;top:3405px;width:1200px;height:371px;background:var(--teal);color:var(--white);font-family:'Arimo',sans-serif}
.footer-lead{position:absolute;left:123px;top:62px;width:990px;font:400 23px/33px 'Arimo',sans-serif}
.footer-contact{position:absolute;left:127px;top:164px;font:400 15px/30px 'Lato',sans-serif}
.footer-contact a,.footer-note a{color:var(--white);text-decoration:underline}
.footer-note{position:absolute;left:125px;top:234px;width:520px;font:400 15px/30px 'Lato',sans-serif}
.legal{left:0;top:3776px;width:1200px;height:43px;background:var(--bar);color:#e6e6e6;display:flex;align-items:center;justify-content:center;font:400 15px 'Lato',sans-serif}
</style>
</head>
<body>

<!-- hero -->
<div class="abs hero"></div>
<div class="abs hero-photo" role="img" aria-label="Smiling nurse in teal scrubs comforting an elderly patient in a wheelchair"></div>

<header>
  <div class="abs brand"><span class="brand-dot"></span>marlow care partners</div>
  <nav class="abs nav"><span>About Us</span><span>For Patients</span><span>For Providers</span><span>Locations</span></nav>
  <a class="btn nav-book">Book Online</a>
</header>

<h1 class="abs hero-title"><span>Marlow</span> Care Partners</h1>
<p class="abs hero-sub">Online appointment booking now<br>available to all patients</p>
<a class="btn hero-book">Book Online</a>

<div class="tile" style="left:116px">Locations<span class="tile-arrow"><svg width="26" height="22" viewBox="0 0 26 22"><path d="M2 11h20M13 2l9 9-9 9" stroke="#35d3dc" stroke-width="3.5" fill="none" stroke-linecap="round" stroke-linejoin="round"/></svg></span></div>
<div class="tile" style="left:458px">Services<span class="tile-arrow"><svg width="26" height="22" viewBox="0 0 26 22"><path d="M2 11h20M13 2l9 9-9 9" stroke="#35d3dc" stroke-width="3.5" fill="none" stroke-linecap="round" stroke-linejoin="round"/></svg></span></div>
<div class="tile" style="left:799px">Contact Us<span class="tile-arrow"><svg width="26" height="22" viewBox="0 0 26 22"><path d="M2 11h20M13 2l9 9-9 9" stroke="#35d3dc" stroke-width="3.5" fill="none" stroke-linecap="round" stroke-linejoin="round"/></svg></span></div>

<!-- about -->
<div class="abs about-frame-top"></div>
<div class="abs about-frame-left"></div>
<div class="abs about-photo" role="img" aria-label="Smiling female doctor with stethoscope in front of colleagues in white coats"></div>
<section class="abs about-card">
  <h2>About Marlow Care Partners</h2>
  <h3>Lorem Ipsum is simply dummy text of the printing and typesetting industry.</h3>
  <p>Lorem Ipsum has been the industry's standard dummy text ever since the 1500s, when an unknown printer took a galley of type and scrambled it to make a type specimen book. It has survived not only five centuries, but also the leap into electronic typesetting, remaining essentially unchanged. It was popularised in the 1960s with the release of Ipsum.</p>
</section>
<a class="btn about-more">Learn More</a>

<!-- services -->
<div class="abs band" style="top:1609px;height:669px"></div>
<h2 class="section-title" style="top:1655px">Management Services</h2>

<svg class="carousel-arrow" style="left:44px;top:1962px" width="32" height="20" viewBox="0 0 32 20"><path d="M30 10H4M11 3l-7 7 7 7" stroke="#1e2a2d" stroke-width="2.5" fill="none"/><path d="M4 10h10" stroke="#35d3dc" stroke-width="4"/></svg>
<svg class="carousel-arrow" style="left:1132px;top:1962px" width="32" height="20" viewBox="0 0 32 20"><path d="M2 10h26M21 3l7 7-7 7" stroke="#1e2a2d" stroke-width="2.5" fill="none"/><path d="M18 10h10" stroke="#35d3dc" stroke-width="4"/></svg>

<div class="svc" style="left:117px;height:504px">
  <div class="svc-icon"><svg width="50" height="50" viewBox="0 0 50 50"><rect x="10" y="6" width="30" height="38" rx="3" fill="none" stroke="#fff" stroke-width="3"/><circle cx="25" cy="20" r="7" fill="none" stroke="#fff" stroke-width="3"/><path d="M16 33h18M16 38h12" stroke="#fff" stroke-width="3"/></svg></div>
  <h4>Billing</h4>
  <ul>
    <li><svg width="16" height="16" viewBox="0 0 16 16"><path d="M3 1v4c0 5 3 7 9 7M9 9l3 3-3 3" stroke="#35d3dc" stroke-width="2" fill="none"/></svg>Provincial Plan</li>
    <li><svg width="16" height="16" viewBox="0 0 16 16"><path d="M3 1v4c0 5 3 7 9 7M9 9l3 3-3 3" stroke="#35d3dc" stroke-width="2" fill="none"/></svg>Workers' Comp</li>
    <li><svg width="16" height="16" viewBox="0 0 16 16"><path d="M3 1v4c0 5 3 7 9 7M9 9l3 3-3 3" stroke="#35d3dc" stroke-width="2" fill="none"/></svg>Federal Police</li>
    <li><svg width="16" height="16" viewBox="0 0 16 16"><path d="M3 1v4c0 5 3 7 9 7M9 9l3 3-3 3" stroke="#35d3dc" stroke-width="2" fill="none"/></svg>Auto Claims</li>
    <li><svg width="16" height="16" viewBox="0 0 16 16"><path d="M3 1v4c0 5 3 7 9 7M9 9l3 3-3 3" stroke="#35d3dc" stroke-width="2" fill="none"/></svg>Medi-Legal</li>
    <li><svg width="16" height="16" viewBox="0 0 16 16"><path d="M3 1v4c0 5 3 7 9 7M9 9l3 3-3 3" stroke="#35d3dc" stroke-width="2" fill="none"/></svg>Patient-paid/3rd party insurance</li>
  </ul>
</div>

<div class="svc active" style="left:457px;height:395px">
  <div class="svc-icon"><svg width="50" height="50" viewBox="0 0 50 50"><circle cx="17" cy="13" r="4" fill="#35d3dc"/><circle cx="25" cy="11" r="4" fill="#35d3dc"/><circle cx="33" cy="13" r="4" fill="#35d3dc"/><path d="M12 28v-8h10v8M20 26v-9h10v9M28 28v-8h10v8" fill="#35d3dc"/><path d="M5 36c8 0 12 4 20 4s12-3 20-8" stroke="#35d3dc" stroke-width="3" fill="none"/></svg></div>
  <h4>Human Resources</h4>
  <ul>
    <li><svg width="16" height="16" viewBox="0 0 16 16"><path d="M3 1v4c0 5 3 7 9 7M9 9l3 3-3 3" stroke="#fff" stroke-width="2" fill="none"/></svg>Employee/Provider recruitment, performance managment</li>
    <li><svg width="16" height="16" viewBox="0 0 16 16"><path d="M3 1v4c0 5 3 7 9 7M9 9l3 3-3 3" stroke="#fff" stroke-width="2" fill="none"/></svg>Policies and Procedures</li>
    <li><svg width="16" height="16" viewBox="0 0 16 16"><path d="M3 1v4c0 5 3 7 9 7M9 9l3 3-3 3" stroke="#fff" stroke-width="2" fill="none"/></svg>Employment Contracts</li>
  </ul>
</div>

<div class="svc" style="left:795px;height:395px">
  <div class="svc-icon"><svg width="50" height="50" viewBox="0 0 50 50"><rect x="15" y="6" width="20" height="38" rx="4" fill="none" stroke="#fff" stroke-width="3"/><rect x="20" y="16" width="10" height="10" fill="none" stroke="#fff" stroke-width="2.5"/><path d="M22 38h6" stroke="#fff" stroke-width="3"/></svg></div>
  <h4>Patient Engagement</h4>
  <ul>
    <li><svg width="16" height="16" viewBox="0 0 16 16"><path d="M3 1v4c0 5 3 7 9 7M9 9l3 3-3 3" stroke="#35d3dc" stroke-width="2" fill="none"/></svg>Intake/Aquisition</li>
    <li><svg width="16" height="16" viewBox="0 0 16 16"><path d="M3 1v4c0 5 3 7 9 7M9 9l3 3-3 3" stroke="#35d3dc" stroke-width="2" fill="none"/></svg>Escallations</li>
    <li><svg width="16" height="16" viewBox="0 0 16 16"><path d="M3 1v4c0 5 3 7 9 7M9 9l3 3-3 3" stroke="#35d3dc" stroke-width="2" fill="none"/></svg>Marketing</li>
    <li><svg width="16" height="16" viewBox="0 0 16 16"><path d="M3 1v4c0 5 3 7 9 7M9 9l3 3-3 3" stroke="#35d3dc" stroke-width="2" fill="none"/></svg>Branding</li>
  </ul>
</div>

<!-- access -->
<h2 class="section-title" style="top:2373px">Easy Access To Care When You Need It</h2>
<p class="abs access-copy">It is a long established fact that a reader will be distracted by the readable content of a page when looking at its layout. The point of using Lorem Ipsum is that it has a more-or-less normal distribution of letters, as opposed to using 'Content here, content here', making it look like readable English.</p>

<div class="access-card" style="left:319px">
  <div class="access-art" role="img" aria-label="Line illustration of a patient resting in a hospital bed"></div>
  <h4>For Patients</h4>
  <a class="btn">Click Here</a>
</div>
<div class="access-card" style="left:636px">
  <div class="access-art" role="img" aria-label="Line illustration of a group of healthcare providers"></div>
  <h4>For Providers</h4>
  <a class="btn">Click Here</a>
</div>

<!-- testimonials -->
<div class="abs band" style="top:2929px;height:476px"></div>
<h2 class="section-title" style="top:2984px">What Do Our Partners Have To Say</h2>

<svg class="carousel-arrow" style="left:44px;top:3180px" width="32" height="20" viewBox="0 0 32 20"><path d="M30 10H4M11 3l-7 7 7 7" stroke="#1e2a2d" stroke-width="2.5" fill="none"/><path d="M4 10h10" stroke="#35d3dc" stroke-width="4"/></svg>
<svg class="carousel-arrow" style="left:1132px;top:3180px" width="32" height="20" viewBox="0 0 32 20"><path d="M2 10h26M21 3l7 7-7 7" stroke="#1e2a2d" stroke-width="2.5" fill="none"/><path d="M18 10h10" stroke="#35d3dc" stroke-width="4"/></svg>

<article class="quote" style="left:120px">
  <div class="quote-photo" role="img" aria-label="Portrait of a smiling man in a dark jacket"></div>
  <div class="quote-name">Daniel Reyes</div>
  <div class="quote-role">Lorem Ipsum</div>
  <div class="quote-rule"></div>
  <p class="quote-text">“Contrary to popular belief, Lorem Ipsum is not simply random text. It has roots in a piece of classical Latin literature from 45 BC, making it over 2000 years old. Richard Mallory, a Latin professor at Ashford College, looked up a few words, consectetur,”</p>
</article>
<article class="quote" style="left:627px">
  <div class="quote-photo" role="img" aria-label="Portrait of a smiling man in a suit with arms crossed"></div>
  <div class="quote-name">Tobin Vasquell</div>
  <div class="quote-role">Lorem Ipsum</div>
  <div class="quote-rule"></div>
  <p class="quote-text" style="top:37px">There are many variations of passages of Lorem Ipsum available, but the majority have suffered alteration in some form, by injected humour, or randomised words which don't look even slightly believable.</p>
</article>

<!-- footer -->
<footer class="abs footer">
  <p class="footer-lead">Marlow Care Partners is focused on our patients first. Connect with us to stay up to date with current news and upcoming events.</p>
  <p class="footer-contact"><a>hello@marlowcarepartners.ca</a><br><a>Phone: 604.555.0142</a></p>
  <p class="footer-note">Please do not send medical questions to this email. If you have a medical question, contact your doctor's office directly. Visit our locations page or click <a>here</a> to find contact information for each of our locations.</p>
</footer>
<div class="abs legal">2022 Marlow Care Partners. All Rights Reserved.</div>

</body>
</html>
```